タイトル 「週末ガーデナーのための水やり流・花咲かせ節約術」
サブタイトル 「毎日が楽になる5つの習慣」

上記の表紙デザインをお願いします。基本お任せします。
本の内容  原稿を添付します。

その他ご不明な点がございましたらお気楽にご質問ください。よろしくお願いいたします。
著者名 星空ナビゲーター 森川佳代 from神戸

本の内容とよくマッチしたデザインだと思いました。インパクトもあり本の対象であるアラフォーの好みと合っているように思いました。

沢山のご応募ありがとうございました。何もかもか初めての作業で、不安でしたが、関心を持っていただいて心からありがたく思っております。これからも電子書籍の出版を考えております。ご縁がありましたらまた、今後もよろしくお願いします。
ありがとうございました。

```html
<!DOCTYPE html>
<html lang="ja">
<head>
<meta charset="UTF-8">
<title>週末ガーデナーのための水やり流・花咲かせ節約術</title>
<link rel="stylesheet" href="https://fonts.googleapis.com/css2?family=Noto+Sans+JP:wght@500;700;900&display=swap">
<style>
  :root {
    --red: #c8232c;
    --ink: #1e1a1a;
    --paper: #ffffff;
    --art-light: #f7eee9;
    --art-mid: #ecd3c9;
  }
  * { margin: 0; padding: 0; box-sizing: border-box; }
  html, body { width: 750px; height: 1200px; overflow: hidden; background: var(--paper); }
  .cover {
    position: relative;
    width: 750px;
    height: 1200px;
    background: var(--paper);
    font-family: "Noto Sans JP", sans-serif;
    overflow: hidden;
  }
  .frame { position: absolute; inset: 0; }
  .title {
    position: absolute;
    left: 110px;
    top: 48px;
    width: 600px;
    text-align: center;
    font-weight: 900;
    line-height: 1;
  }
  .title-line { display: block; white-space: nowrap; letter-spacing: 0.02em; }
  .title-line--lead  { font-size: 74px; color: var(--red); }
  .title-line--for   { font-size: 74px; color: var(--ink); margin-top: 16px; }
  .title-line--style { font-size: 74px; color: var(--ink); margin-top: 16px; }
  .title-line--main  { font-size: 80px; color: var(--red); margin-top: 24px; }
  .author {
    position: absolute;
    left: 54px;
    top: 228px;
    height: 770px;
    writing-mode: vertical-rl;
    font-weight: 700;
    font-size: 30px;
    line-height: 1;
    color: var(--red);
    letter-spacing: 0.06em;
    white-space: nowrap;
  }
  .author__place { font-size: 26px; }
  .illustration {
    position: absolute;
    left: 120px;
    top: 480px;
    width: 590px;
    height: 530px;
    border-radius: 200px 200px 0 0;
    background: linear-gradient(180deg, var(--art-light), var(--art-mid));
  }
  .band {
    position: absolute;
    left: 0; right: 0; bottom: 0;
    height: 190px;
    background: var(--red);
  }
  .subtitle {
    position: absolute;
    left: 28px;
    top: 1026px;
    color: var(--paper);
    font-weight: 900;
    line-height: 1;
  }
  .subtitle__lead { display: block; font-size: 40px; margin-left: 60px; }
  .subtitle__main { display: block; margin-top: 14px; font-size: 84px; white-space: nowrap; }
  .subtitle__num { font-size: 120px; vertical-align: -6px; margin-right: 6px; }
  .tagline {
    position: absolute;
    left: 500px;
    top: 1030px;
    width: 240px;
    height: 148px;
    background: var(--paper);
    border-radius: 18px;
    color: var(--red);
    font-weight: 900;
    font-size: 32px;
    line-height: 1.3;
    text-align: center;
    display: flex;
    align-items: center;
    justify-content: center;
  }
</style>
</head>
<body>
<main class="cover">
  <svg class="frame" width="750" height="1200" viewBox="0 0 750 1200" aria-hidden="true">
    <path d="M22 1015 V70 Q22 22 70 22 H680 Q728 22 728 70 V1015" fill="none" stroke="var(--red)" stroke-width="12"/>
    <path d="M42 1015 V84 Q42 42 84 42 H666 Q708 42 708 84 V1015" fill="none" stroke="var(--red)" stroke-width="3"/>
  </svg>

  <h1 class="title">
    <span class="title-line title-line--lead">週末ガーデナー</span>
    <span class="title-line title-line--for">のための</span>
    <span class="title-line title-line--style">水やり流</span>
    <span class="title-line title-line--main">花咲かせ節約術</span>
  </h1>

  <p class="author">著者　星空ナビゲーター　森川佳代　<span class="author__place">from神戸</span></p>

  <div class="illustration" role="img" aria-label="庭仕事をする二人と花、水引飾りのイラスト"></div>

  <div class="band"></div>
  <p class="subtitle">
    <span class="subtitle__lead">毎日が楽になる</span>
    <span class="subtitle__main"><span class="subtitle__num">5</span>つの習慣</span>
  </p>
  <p class="tagline">この1冊で<br>節約の秘訣<br>まるわかり!</p>
</main>
</body>
</html>
```